New Healthy Dog Treat Business Needs Product Lable

We are a start up business that produces hand made healthy treats for dogs. All of a products are based on human grade ingredients and we pride ourselves on ensuring that we do not add any salt, sugar or preservatives to our products. We need a label designed for our treats to be used on multiple products.

Please view our website for any additional information and details

www.wrenlybakehouse.com.au

Target Market(s)

Dog Lovers who care about the quality of the treats that they feed their dogs.

Industry/Entity Type

Business

Font styles to use
Serif

Requirements
Must have
• Use our logo or at least part of the logo ie the vector file.
• Must be 8 cm high and 10 cm wide
• State that the product needs to be Stored in the Fridge or be Refridgerated to retain that just baked Freshenss.
• Must say (Pet Food Only)
• Should mention Website Address - www.wrenlybakehouse.com.au
• email and phone contacts.
Nice to have
• Would like to have reference to the following items -
• Handmade
• Human Grade Ingredients
• No preservative, Salt or Sugar
• We would ideally like two versions of the label one with Artisan Baked Biscuits, and the other with Artisan Baked Biscotti this way we can add the relevant varieties with a small sticker below.

```html
<!DOCTYPE html>
<html lang="en">
<head>
<meta charset="utf-8">
<title>Wrenly Bakehouse – Healthy Dog Treats Label</title>
<link rel="stylesheet" href="https://fonts.googleapis.com/css2?family=Open+Sans:wght@400;600;800&display=swap">
<style>
  :root {
    --canvas-bg: #d6ebe6;
    --label-red: #d8361c;
    --frame-dark: #2b2421;
    --panel-dark: #2b2421;
    --dash-tan: #c9a273;
    --ribbon-tan: #c7b597;
    --ribbon-text: #2b2421;
    --cream: #ece2d3;
    --gold: #d9a86a;
    --white: #ffffff;
    --art-green: #6cc04a;
    --art-orange: #e98a2c;
  }
  * { box-sizing: border-box; margin: 0; padding: 0; }
  html, body { width: 1200px; height: 960px; overflow: hidden; }
  body {
    background: var(--canvas-bg);
    font-family: "Open Sans", Arial, sans-serif;
    position: relative;
  }
  .label {
    position: absolute;
    left: 100px; top: 80px;
    width: 1000px; height: 800px;
    background: var(--label-red);
  }
  .label__frame {
    position: absolute;
    inset: 23px;
    background: var(--frame-dark);
    padding: 12px;
    display: flex;
    flex-direction: column;
  }
  .hero {
    position: relative;
    height: 460px;
    background: var(--label-red);
  }
  .brand-name {
    position: absolute;
    top: 30px; left: 0; right: 0;
    text-align: center;
    color: var(--white);
    font-weight: 800;
    font-size: 64px;
    line-height: 1;
  }
  .hero__art {
    position: absolute;
    left: 170px; top: 115px;
    width: 590px; height: 240px;
  }
  .tagline {
    position: absolute;
    bottom: 18px; left: 0; right: 0;
    text-align: center;
    color: var(--white);
    font-weight: 800;
    font-size: 60px;
    line-height: 1;
    letter-spacing: -0.5px;
  }
  .info {
    flex: 1;
    background: var(--panel-dark);
    padding: 14px 20px 12px;
  }
  .info__box {
    position: relative;
    height: 100%;
    border: 2px dashed var(--dash-tan);
    border-radius: 10px;
  }
  .benefits {
    position: absolute;
    left: 24px; right: 24px; top: 14px;
    color: var(--cream);
    font-size: 25px;
    white-space: nowrap;
    padding-bottom: 8px;
    border-bottom: 1px solid var(--dash-tan);
  }
  .ribbon {
    position: absolute;
    left: 190px; top: 76px;
    width: 520px; height: 56px;
  }
  .ribbon__text {
    position: absolute;
    inset: 0;
    display: flex; align-items: center; justify-content: center;
    color: var(--ribbon-text);
    font-size: 28px;
    font-weight: 600;
    letter-spacing: 0.5px;
  }
  .storage {
    position: absolute;
    left: 24px; top: 152px;
    color: var(--gold);
    font-size: 23px;
  }
  .pet-only {
    position: absolute;
    left: 24px; top: 196px;
    display: flex; align-items: center; gap: 10px;
    color: var(--gold);
    font-size: 23px;
  }
  .pet-only__icon {
    width: 30px; height: 26px;
    background: var(--gold);
    border-radius: 5px;
  }
  .contact {
    position: absolute;
    right: 26px; top: 160px;
    text-align: right;
    color: var(--white);
    font-size: 19px;
    line-height: 1.3;
  }
</style>
</head>
<body>
  <section class="label">
    <div class="label__frame">
      <header class="hero">
        <h1 class="brand-name">Wrenly Bakehouse</h1>
        <svg class="hero__art" viewBox="0 0 590 240" role="img" aria-label="Illustration of a chef dog mascot with pumpkin, greens, apples, oats and nuts beside an artisan baked oven badge">
          <defs>
            <radialGradient id="artFill" cx="50%" cy="45%" r="60%">
              <stop offset="0%" stop-color="var(--art-orange)"/>
              <stop offset="100%" stop-color="var(--art-green)"/>
            </radialGradient>
          </defs>
          <ellipse cx="295" cy="120" rx="290" ry="118" fill="url(#artFill)"/>
        </svg>
        <p class="tagline">HEALTHY DOG TREATS</p>
      </header>
      <div class="info">
        <div class="info__box">
          <p class="benefits">Handmade |Human Grade Ingredients |No preservative, Salt or Sugar</p>
          <div class="ribbon">
            <svg width="520" height="56" viewBox="0 0 520 56" aria-hidden="true">
              <polygon points="0,0 520,0 504,28 520,56 0,56 16,28" fill="var(--ribbon-tan)"/>
            </svg>
            <span class="ribbon__text">ARTISAN BAKED BISCUITS</span>
          </div>
          <p class="storage">Stored in the Fridge</p>
          <p class="pet-only"><span class="pet-only__icon" role="img" aria-label="Dog icon"></span>Pet Food Only</p>
          <address class="contact" style="font-style:normal">
            www.wrenlybakehouse.com.au<br>
            hello@wrenlybakehouse.com.au<br>
            + 0491 570 156
          </address>
        </div>
      </div>
    </div>
  </section>
</body>
</html>
```